Antigen Preservation Bureau

The company will provide a contract research services to stabilize various viruses, viral vectors, and vaccines. It may offer some licensing opportunities for stabilizing technologies. Main area of applications are pharmaceutical, therapeutic, and vaccination field. The company aspires to develop room temperature vaccines for global distribution beyond the current cold chain.

Target Market(s)

pharmaceutical, therapeutic and vaccination fields

Coding

Coded - Design and coding required

Number of Pages Required

4 page

Requirements
Must have
• Incorporate a APB logo, attached at the bottom, on the Web page

```html
<!DOCTYPE html>
<html lang="en">
<head>
<meta charset="utf-8">
<title>Antigen Preservation Bureau</title>
<link href="https://fonts.googleapis.com/css2?family=Source+Sans+3:wght@300;400;600;700&family=Playfair+Display:wght@700&display=swap" rel="stylesheet">
<style>
:root{
  --green:#3b8f72;
  --gold:#c8922f;
  --dark:#262a31;
  --ink:#2b2b2b;
  --muted:#6b6b6b;
  --light:#eef0f2;
  --white:#ffffff;
}
*{box-sizing:border-box;margin:0;padding:0}
html,body{width:1200px;height:3879px;overflow:hidden}
body{position:relative;background:var(--white);font-family:"Source Sans 3",Arial,sans-serif;color:var(--ink)}
.abs{position:absolute}
.shape{position:absolute;left:0;top:0}
/* header */
.site-header{position:absolute;left:0;top:0;width:1200px;height:68px;background:var(--white)}
.brand{position:absolute;left:150px;top:16px;display:flex;align-items:center;gap:10px}
.brand-mark{width:34px;height:34px;background:var(--green)}
.brand-name{font-size:13px;font-weight:600;letter-spacing:1.5px;text-transform:uppercase;color:var(--green);line-height:1.2;width:150px}
.main-nav{position:absolute;right:150px;top:22px;display:flex;align-items:center;gap:30px;font-size:12px;font-weight:600;text-transform:uppercase;color:var(--ink)}
.nav-cta{background:var(--gold);color:var(--white);padding:6px 14px;border-radius:14px}
.call-bar{position:absolute;left:0;top:68px;width:1200px;height:56px;background:var(--light);text-align:right;padding:16px 150px 0 0;font-size:17px;font-weight:600;color:var(--ink)}
.call-bar b{color:var(--green)}
/* hero */
.hero-text{position:absolute;right:150px;top:438px;text-align:right;color:var(--white);text-transform:uppercase}
.hero-text .l1{font-size:38px;font-weight:300;line-height:46px}
.hero-text .l2{font-size:46px;font-weight:700;line-height:52px}
.hero-text .l3{font-size:28px;font-weight:300;line-height:36px}
.btn-outline{display:inline-block;border:1.5px solid var(--white);color:var(--white);font-size:13px;font-weight:600;padding:8px 18px;border-radius:18px;text-transform:none}
.hero-text .btn-outline{margin-top:30px}
.tagline{position:absolute;left:0;top:960px;width:1200px;text-align:center}
.tagline .t1{color:var(--white);font-size:34px;font-weight:400}
.tagline .t2{color:var(--gold);font-size:44px;font-weight:400;margin-top:4px}
/* sectors */
.section-title{position:absolute;left:0;width:1200px;text-align:center;font-size:30px;font-weight:600;color:var(--ink)}
.sectors{position:absolute;left:150px;top:1310px;width:900px;display:flex;justify-content:space-between}
.sector{width:215px;text-align:center}
.sector-icon{width:96px;height:96px;margin:0 auto}
.sector h3{font-size:18px;font-weight:600;margin-top:14px}
.sector p,.post p{font-size:11px;color:var(--muted);line-height:15px;margin-top:8px}
.btn-box{position:absolute;width:136px;height:34px;border:1.5px solid var(--ink);font-size:13px;font-weight:600;text-align:center;line-height:31px;color:var(--ink)}
/* about */
.about-text{position:absolute;right:150px;top:1786px;width:520px;text-align:right;color:var(--white)}
.about-text h2{font-size:30px;font-weight:600}
.about-text p{font-size:11px;line-height:16px;margin-top:16px}
.about-text .btn-box{position:static;display:inline-block;border-color:var(--white);color:var(--white);margin-top:44px}
/* blog */
.posts{position:absolute;left:150px;top:2356px;width:900px;display:flex;justify-content:space-between}
.post{width:214px}
.post-image{width:214px;height:160px}
.post time{display:block;font-size:10px;color:var(--ink);margin-top:20px}
.post h3{font-size:14px;font-weight:600;line-height:17px;margin-top:8px}
/* press */
.press{position:absolute;left:150px;top:2818px;width:900px;height:110px;border-top:1px solid #ddd;border-bottom:1px solid #ddd;display:flex;align-items:center;justify-content:space-between}
.arrow-btn{width:24px;height:24px;border:1px solid #ccc;border-radius:50%;display:flex;align-items:center;justify-content:center}
.press-name{font-size:26px;font-weight:700;color:var(--ink)}
/* contact */
.contact{position:absolute;left:150px;top:3140px;width:500px;color:var(--white)}
.contact h2{font-size:30px;font-weight:600}
.field{position:absolute;border-bottom:1px solid rgba(255,255,255,.7);font-size:11px;height:28px}
.contact .btn-box{border-color:var(--white);color:var(--white)}
/* footer */
.footer-brand{position:absolute;left:150px;top:3612px;display:flex;align-items:center;gap:10px}
.footer-brand .brand-mark{background:var(--white)}
.footer-brand .brand-name{color:var(--white)}
.badges{position:absolute;left:150px;top:3700px;display:flex;gap:18px}
.badge{width:42px;height:42px;border:2px solid var(--white)}
.subscribe{position:absolute;left:180px;top:3760px;background:var(--gold);color:var(--white);font-size:11px;font-weight:700;text-transform:uppercase;padding:8px 16px;border-radius:16px}
.footer-col{position:absolute;top:3650px;font-size:12px;color:var(--white);line-height:27px;list-style:none}
.copyright{position:absolute;left:0;top:3840px;width:1200px;height:39px;background:#1c1f24;color:#bbb;font-size:10px;text-align:center;line-height:39px}
</style>
</head>
<body>

<header class="site-header">
  <div class="brand"><span class="brand-mark"></span><span class="brand-name">Antigen Preservation Bureau</span></div>
  <nav class="main-nav">
    <span>Home</span><span>About</span><span>Vaccines ⌄</span><span>Research</span><span>Recent Publications</span><span>Resources</span><span class="nav-cta">Contact Us</span>
  </nav>
</header>
<div class="call-bar">CALL US NOW: <b>1800 555 0142</b></div>

<svg class="shape" width="1200" height="1153" viewBox="0 0 1200 1153">
  <defs>
    <linearGradient id="heroPhoto" x1="0" y1="0" x2="1" y2="1">
      <stop offset="0" stop-color="#e6ecef"/><stop offset=".5" stop-color="#c9d9df"/><stop offset="1" stop-color="#9fb8c4"/>
    </linearGradient>
  </defs>
  <rect x="0" y="124" width="1200" height="768" fill="url(#heroPhoto)" role="img" aria-label="Photo of a researcher giving a vaccination in a lab"/>
  <polygon points="1000,124 1200,124 1200,330 880,600" fill="#ffffff" opacity=".55"/>
  <polygon points="700,410 1200,345 1200,700 610,700" fill="var(--green)"/>
  <polygon points="660,892 760,740 1200,680 1200,892" fill="var(--dark)"/>
  <rect x="0" y="892" width="1200" height="261" fill="var(--dark)"/>
</svg>

<div class="hero-text">
  <div class="l1">Stable Virus</div>
  <div class="l2">Viral Vector</div>
  <div class="l3">and Vaccine Formulation</div>
  <span class="btn-outline">Contact Us Now</span>
</div>

<div class="tagline">
  <div class="t1">Research services provider to stabilize</div>
  <div class="t2">various viruses, viral vectors, and vaccines.</div>
</div>

<h2 class="section-title" style="top:1228px">Our Main Research Sectors</h2>
<div class="sectors">
  <div class="sector">
    <svg class="sector-icon" viewBox="0 0 96 96" role="img" aria-label="Virus icon"><polygon points="48,4 86,26 86,70 48,92 10,70 10,26" fill="var(--dark)"/><circle cx="48" cy="48" r="22" fill="var(--gold)"/></svg>
    <h3>Viruses stabilization</h3>
    <p>Curabitur suscipit, eros rutrum iaculis vestibulum, mi mi tincidunt ante, sed dignissim urna leo eget velit. Vestibulum vitae iaculis dolor.</p>
  </div>
  <div class="sector">
    <svg class="sector-icon" viewBox="0 0 96 96" role="img" aria-label="DNA icon"><polygon points="48,4 86,26 86,70 48,92 10,70 10,26" fill="var(--dark)"/><circle cx="48" cy="48" r="22" fill="var(--green)"/></svg>
    <h3>Viral vectors</h3>
    <p>Curabitur suscipit, eros rutrum iaculis vestibulum, mi mi tincidunt ante, sed dignissim urna leo eget velit. Vestibulum vitae iaculis dolor.</p>
  </div>
  <div class="sector">
    <svg class="sector-icon" viewBox="0 0 96 96" role="img" aria-label="Syringe icon"><polygon points="48,4 86,26 86,70 48,92 10,70 10,26" fill="var(--dark)"/><circle cx="48" cy="48" r="22" fill="var(--gold)"/></svg>
    <h3>Vaccines</h3>
    <p>Curabitur suscipit, eros rutrum iaculis vestibulum, mi mi tincidunt ante, sed dignissim urna leo eget velit. Vestibulum vitae iaculis dolor.</p>
  </div>
  <div class="sector">
    <svg class="sector-icon" viewBox="0 0 96 96" role="img" aria-label="Vaccine vial icon"><polygon points="48,4 86,26 86,70 48,92 10,70 10,26" fill="var(--dark)"/><circle cx="48" cy="48" r="22" fill="var(--green)"/></svg>
    <h3>Room temperature vaccines</h3>
    <p>Curabitur suscipit, eros rutrum iaculis vestibulum, mi mi tincidunt ante, sed dignissim urna leo eget velit. Vestibulum vitae iaculis dolor.</p>
  </div>
</div>
<div class="btn-box" style="left:532px;top:1546px">Explore More</div>

<svg class="shape" width="1200" height="2290" viewBox="0 0 1200 2290">
  <defs>
    <linearGradient id="aboutPhoto" x1="0" y1="0" x2="1" y2="0">
      <stop offset="0" stop-color="#d7e6ee"/><stop offset=".6" stop-color="#7fa9c4"/><stop offset="1" stop-color="#3f6d93"/>
    </linearGradient>
  </defs>
  <polygon points="0,1610 1200,1720 1200,2180 0,2270" fill="url(#aboutPhoto)" role="img" aria-label="Photo of a hand holding a syringe beside a vaccine vial"/>
  <polygon points="0,1603 1200,1603 1200,1710 0,1620" fill="#ffffff"/>
  <polygon points="315,1766 1200,1686 1200,2162 580,1950" fill="var(--gold)"/>
</svg>

<div class="about-text">
  <h2>About Antigen Preservation Bureau</h2>
  <p>Aenean vehicula augue non nisi pulvinar, ut porttitor nulla dapibus. Donec semper lobortis enim, vitae sodales lacus. Quisque elit leo, interdum vitae risus ac, elementum tincidunt arcu. Maecenas ac iaculis neque. Vivamus iaculis et amet tempus sed laoreet.</p>
  <p>Maecenas ac nisl vitae purus placerat faucibus sit amet non ligula. Duis quis felis nisi. Pellentesque habitant morbi tristique senectus et netus et malesuada fames ac turpis egestas donec quam.</p>
  <span class="btn-box">Explore More</span>
</div>

<h2 class="section-title" style="top:2300px">Our Blog</h2>
<div class="posts">
  <article class="post">
    <div class="post-image" role="img" aria-label="Photo of lab samples under a microscope" style="background:linear-gradient(135deg,#9ed3e0,#3c94ad)"></div>
    <time>4 January, 2019</time>
    <h3>Maecenas bibendum, massa sollic tudin fringilla velit sed egestas frin gilla.</h3>
    <p>Curabitur suscipit, eros rutrum iaculis vestibulum, mi mi tincidunt ante, sed dignissim urna leo eget velit. Vestibulum vitae iaculis dolor.</p>
  </article>
  <article class="post">
    <div class="post-image" role="img" aria-label="Photo of a laboratory centrifuge" style="background:linear-gradient(135deg,#c7d3da,#4b6272)"></div>
    <time>4 January, 2019</time>
    <h3>Maecenas bibendum, massa sollic tudin fringilla velit sed egestas frin gilla.</h3>
    <p>Curabitur suscipit, eros rutrum iaculis vestibulum, mi mi tincidunt ante, sed dignissim urna leo eget velit. Vestibulum vitae iaculis dolor.</p>
  </article>
  <article class="post">
    <div class="post-image" role="img" aria-label="Photo of gloved hands holding a petri dish" style="background:linear-gradient(135deg,#5b7fd6,#1d3f9a)"></div>
    <time>4 January, 2019</time>
    <h3>Maecenas bibendum, massa sollic tudin fringilla velit sed egestas frin gilla.</h3>
    <p>Curabitur suscipit, eros rutrum iaculis vestibulum, mi mi tincidunt ante, sed dignissim urna leo eget velit. Vestibulum vitae iaculis dolor.</p>
  </article>
  <article class="post">
    <div class="post-image" role="img" aria-label="Photo of researchers working in a laboratory" style="background:linear-gradient(135deg,#dfe8ee,#7a97ad)"></div>
    <time>4 January, 2019</time>
    <h3>Maecenas bibendum, massa sollic tudin fringilla velit sed egestas frin gilla.</h3>
    <p>Curabitur suscipit, eros rutrum iaculis vestibulum, mi mi tincidunt ante, sed dignissim urna leo eget velit. Vestibulum vitae iaculis dolor.</p>
  </article>
</div>
<div class="btn-box" style="left:532px;top:2716px">Explore More</div>

<div class="press">
  <span class="arrow-btn"><svg width="8" height="10" viewBox="0 0 8 10"><path d="M6 1 2 5l4 4" stroke="#555" fill="none" stroke-width="1.5"/></svg></span>
  <span class="press-name">The Daily Ledger</span>
  <span class="press-name">MJR</span>
  <span class="press-name">Riverton Courier</span>
  <span class="press-name">Coastal Times</span>
  <span class="arrow-btn"><svg width="8" height="10" viewBox="0 0 8 10"><path d="M2 1l4 4-4 4" stroke="#555" fill="none" stroke-width="1.5"/></svg></span>
</div>

<svg class="shape" width="1200" height="3879" viewBox="0 0 1200 3879">
  <defs>
    <linearGradient id="labPhoto" x1="0" y1="0" x2="1" y2="1">
      <stop offset="0" stop-color="#d8e4ea"/><stop offset=".5" stop-color="#9fb3bf"/><stop offset="1" stop-color="#4e5f6b"/>
    </linearGradient>
  </defs>
  <polygon points="760,3005 1200,3005 1200,3660 640,3640" fill="url(#labPhoto)" role="img" aria-label="Photo of pipettes dispensing green liquid into a petri dish"/>
  <polygon points="0,3090 880,3040 780,3520 0,3560" fill="var(--green)"/>
  <polygon points="0,3560 800,3520 1200,3600 1200,3879 0,3879" fill="var(--dark)"/>
</svg>

<div class="contact"><h2>Contact Us</h2></div>
<div class="field" style="left:150px;top:3210px;width:215px;color:#fff">Name</div>
<div class="field" style="left:435px;top:3210px;width:215px;color:#fff">E-mail</div>
<div class="field" style="left:150px;top:3285px;width:500px;height:86px;color:#fff">Message</div>
<div class="btn-box" style="left:150px;top:3412px;border-color:#fff;color:#fff">Contact Us</div>

<div class="footer-brand"><span class="brand-mark"></span><span class="brand-name">Antigen Preservation Bureau</span></div>
<div class="badges"><span class="badge"></span><span class="badge"></span><span class="badge"></span><span class="badge"></span></div>
<div class="subscribe">Subscribe to Newsletter</div>
<ul class="footer-col" style="left:500px"><li>Immunization</li><li>Diseases</li><li>Vaccines</li><li>Health Professionals</li></ul>
<ul class="footer-col" style="left:690px"><li>Home</li><li>About Us</li><li>Vaccines</li><li>Research</li></ul>
<ul class="footer-col" style="left:836px"><li>Recent Publications</li><li>Resources</li><li>Contact Us</li></ul>
<div class="copyright">© 2019 Antigen Preservation Bureau. All Rights Reserved.</div>

</body>
</html>
```